Letterhead for SaaS

Design a letterhead that aligns with our new business card, using our logo and color scheme and text defined in the Branding Guide to ensure consistency. Consider incorporating a subtle watermark for added elegance. The layout should reflect the card's style, creating a cohesive look across our stationery.

```html
<!DOCTYPE html>
<html lang="en">
<head>
<meta charset="utf-8">
<title>Norvale Letterhead</title>
<link href="https://fonts.googleapis.com/css2?family=Mulish:wght@600;700;800&family=Arimo:wght@400&family=Allura&display=swap" rel="stylesheet">
<style>
  :root {
    --backdrop: #e4e4e4;
    --paper: #ffffff;
    --ink: #1b1f2a;
    --text: #4a4a4a;
    --rule: #9a9a9a;
    --accent: #00c2f8;
  }
  * { margin: 0; padding: 0; box-sizing: border-box; }
  html, body {
    width: 1153px;
    height: 1200px;
    overflow: hidden;
    background: var(--backdrop);
  }
  .sheet {
    position: absolute;
    left: 241px;
    top: 125px;
    width: 671px;
    height: 950px;
    background: var(--paper);
  }
  .brand {
    position: absolute;
    top: 112px;
    left: 0;
    width: 100%;
    display: flex;
    justify-content: center;
    align-items: center;
    gap: 10px;
  }
  .brand-dot {
    width: 26px;
    height: 26px;
    border-radius: 50%;
    background: var(--ink);
  }
  .brand-name {
    font-family: "Mulish", sans-serif;
    font-weight: 800;
    font-size: 21px;
    letter-spacing: 0.5px;
    color: var(--ink);
  }
  .letter {
    position: absolute;
    left: 60px;
    top: 290px;
    width: 552px;
  }
  .salutation {
    font-family: "Mulish", sans-serif;
    font-weight: 700;
    font-size: 16px;
    color: var(--text);
    margin-bottom: 24px;
  }
  .body-copy p {
    font-family: "Arimo", Arial, sans-serif;
    font-size: 11.6px;
    line-height: 13.8px;
    color: var(--text);
    margin-bottom: 12.5px;
  }
  .closing {
    font-family: "Mulish", sans-serif;
    font-weight: 700;
    font-size: 9px;
    color: var(--ink);
    margin-top: 22px;
    margin-left: 1px;
  }
  .signature {
    font-family: "Allura", cursive;
    font-size: 26px;
    color: var(--ink);
    margin-top: 26px;
    margin-left: -4px;
  }
  .footer-rule {
    position: absolute;
    left: 144px;
    width: 383px;
    top: 898px;
    border-top: 1px solid var(--rule);
  }
  .contacts {
    position: absolute;
    top: 905px;
    left: 0;
    width: 100%;
    display: flex;
    justify-content: center;
    gap: 11px;
    font-family: "Arimo", Arial, sans-serif;
    font-size: 11.5px;
    color: var(--text);
  }
  .contact {
    display: flex;
    align-items: center;
    gap: 4px;
  }
  .contact svg { width: 9px; height: 9px; fill: var(--accent); }
  .accent-bar {
    position: absolute;
    left: 0;
    bottom: 0;
    width: 100%;
    height: 8px;
    background: var(--accent);
  }
</style>
</head>
<body>
  <main class="sheet">
    <header class="brand">
      <span class="brand-dot"></span>
      <span class="brand-name">NORVALE</span>
    </header>

    <section class="letter">
      <h1 class="salutation">Dear Mr. Hale,</h1>
      <div class="body-copy">
        <p>Lorem ipsum dolor sit amet, consectetuer adipiscing elit, sed diam nonmmy nibh euismod tincidunt ut laor eet dolore magna aliquam erat volutpat. Ut wisi enim ad minim veniam, quis nostrud exerci tationmcorper suscipit lobortis nisl ut aliquip ex ea commodo consequat. Duis autem vel eum iriure dolor in hendrerit in vulputate velit esse molestie consequat, vel illum dolore eu feugiat</p>
        <p>Rorem ipsum dolor sit amet, consectetuer adipiscing elit, sed diam nonmmy nibh euismod tincidunt ut laor eet dolore magna aliquam erat volutpat. Ut wisi enim ad minim veniam, quis nostrud exerci tationmcorper suscipit lobortis nisl ut aliquip ex ea commodo consequat. Duis autem vel eum iriure dolor in hendrerit in vulputate velit esse molest</p>
        <p>Dorem ipsum dolor sit amet, consectetuer adipiscing elit, sed diam nonmmy nibh euismod tincidunt ut laor eet dolore magna aliquam erat volutpat. Ut wisi enim ad minim veniam, quis nostrud exerci tationmcorper suscipit lobortis nisl ut aliquip ex ea commodo consequat. Duis autem vel eum iriure dolor in hendrerit in suscipit lobortis nisl ut aliquip ex ea commodo consequat. Duis autem vel eum iriure dolor in hendrerit in vulputate velit esse molestie consequat, vel illum</p>
        <p>Sorem ipsum dolor sit amet, consectetuer adipiscing elit, sed diam nonmmy nibh euismod tincidunt ut laor eet dolore magna aliquam erat volutpat. Ut wisi enim ad minim veniam, quis nostrud exerci tationmcorper suscipit lobortis nisl ut aliquip ex ea commodo consequat. Duis autem vel eum iriure dolor in</p>
      </div>
      <p class="closing">Sincerely,</p>
      <p class="signature">Daniel Marsh</p>
    </section>

    <div class="footer-rule"></div>
    <footer class="contacts">
      <span class="contact">
        <svg viewBox="0 0 10 10" aria-hidden="true"><path d="M1 3c0-1 1-2 4-2s4 1 4 2v1H7V3H3v1H1zM2 5h6l1 4H1z"/></svg>
        044-210 387 654
      </span>
      <span class="contact">
        <svg viewBox="0 0 10 10" aria-hidden="true"><path d="M0 2h10v6H0zM1 3v.4l4 2.6 4-2.6V3L5 5.4z"/></svg>
        hello@norvale.io
      </span>
      <span class="contact">
        <svg viewBox="0 0 10 10" aria-hidden="true"><circle cx="5" cy="5" r="5"/></svg>
        www.norvale.io
      </span>
    </footer>
    <div class="accent-bar"></div>
  </main>
</body>
</html>
```